Orsabellitravel.com web design project + logo design

Hi,

We are a Russian online tour operator - tripwelder.com

We are looking to tranmsfer our domain to orsabellitravel.com. The website and logo need to be orsabelliesque - we are not looking to change our functionality, but we need to make the website much more attracitve to clients, much more wild looking but at the same time remaining a professional travel company.

The main concept of the website should be innovative travel (as orsabelli was an innovator). Alternatively, you could go down the artist route and go down the draw / design your own tour road.

On our website the customer is able to combine travel services (hotels, flights, Cardo services, and soon chauffeur, car rental etc...) put it into their basket (the basket definitely has to look better than it is at the moment) and pay for it in one go by card.

We are also stressin our customer support with web chat, call centre etc... (call centre number at the top of the page)

We aim to provide an easy user experience, but we need to make it have some more style, so I will be waiting for what you guys can come up with.
Let me know if you have any questions - skype is: mrkolbuzov

It Company

• It is quite a simple task - to take the existing website tripwelder.com and orsabellisize it to create orsabellitravel.com, the functionality of the website will remain the same and there are not many pages in the website. Homepage, Checkout step1, Checkout step 2 (you can view both of these if you select a service) and the generic pages for T&C''s, Privacy policy etc...

IMPORTANT UPDATE

We are also looking at how the search results will look in the designs, (please do a search on our website for hotel / flight)

```html
<!DOCTYPE html>
<html lang="en">
<head>
<meta charset="utf-8">
<title>Orsabelli travel</title>
<link href="https://fonts.googleapis.com/css2?family=PT+Sans:wght@400;700&display=swap" rel="stylesheet">
<style>
:root{
  --orange:#f47a1f;
  --orange-light:#fb9a35;
  --orange-dark:#e3621a;
  --purple:#8a4bc6;
  --purple-dark:#6a3b78;
  --red:#e4571a;
  --green:#6aa528;
  --text:#6b6b6b;
  --heading:#555;
  --line:#e2e2e2;
  --white:#fff;
}
*{box-sizing:border-box;margin:0;padding:0}
html,body{width:859px;height:1200px;overflow:hidden;background:#fff}
body{position:relative;font-family:"PT Sans",sans-serif;color:var(--text)}
.abs{position:absolute}
.hero{left:0;top:0;width:859px;height:492px;
  background:linear-gradient(180deg,#7cc0ea 0%,#a9d7f2 30%,#3aa9cf 45%,#23b9c4 58%,#6fd0cf 66%,#e9e1cf 80%,#dccdb0 100%)}
.phone{right:60px;top:3px;font-size:10px;line-height:14px;color:#222;white-space:nowrap}
.phone b{font-size:13px}
.topbar{left:54px;top:21px;width:751px;height:79px;background:linear-gradient(180deg,var(--orange-light),var(--orange));box-shadow:0 3px 4px rgba(0,0,0,.2)}
.logo{left:26px;top:26px;display:flex;align-items:center;gap:8px;color:#fff;font-size:28px;white-space:nowrap}
.logo i{display:block;width:18px;height:18px;border-radius:50%;background:#fff}
.nav{left:363px;top:34px;display:flex;align-items:center;color:#fff;font-size:14px;white-space:nowrap}
.nav span{display:flex;align-items:center;padding:0 18px;border-left:1px solid rgba(255,255,255,.45);line-height:18px;height:18px}
.nav span:first-child{border-left:0}
.nav svg{margin-left:3px;margin-top:-6px}
.tab{top:242px;height:32px;border-radius:4px 4px 0 0;color:#fff;font-size:14px;text-align:center;line-height:34px;border:2px solid #fff;border-bottom:0}
.tab.active{background:var(--purple);font-weight:700}
.tab.idle{background:var(--purple-dark)}
.panel{left:54px;top:273px;width:462px;height:176px;background:#fff;border-radius:0 4px 4px 4px;box-shadow:0 2px 6px rgba(0,0,0,.15)}
.lbl{font-size:12px;color:#555}
.field{height:23px;border:1px solid #d5d5d5;border-radius:2px;font-size:9px;color:#999;padding:0 8px;line-height:21px;background:#fff}
.field.val{color:#555}
.sel::after{content:"";position:absolute;right:5px;top:9px;border:4px solid transparent;border-top:5px solid #aaa}
.sel .sep{position:absolute;right:16px;top:3px;bottom:3px;border-left:1px solid #ddd}
.chk{font-size:8px;color:#666;display:flex;align-items:center;gap:4px;white-space:nowrap}
.chk i{display:block;width:10px;height:10px;border:1px solid #bbb;border-radius:2px}
.btn{background:linear-gradient(180deg,#f8893a,var(--red));color:#fff;border-radius:2px;text-align:center;font-size:12px}
.card{top:515px;width:232px;height:180px;border:1px solid var(--line);border-radius:3px;background:linear-gradient(180deg,#fff,#f6f6f6);padding:14px 22px}
.card h2{font-weight:400;font-size:22px;line-height:1.2;margin-bottom:4px}
.card p,.card li{font-size:9.5px;line-height:16.8px}
.card ol{margin-top:8px;padding-left:0;list-style:none;color:#555}
.about{left:55px;top:738px;width:496px}
.about h2,.gallery h2{font-weight:400;font-size:19px;color:var(--heading);margin-bottom:4px}
.about p{font-size:9.8px;line-height:16.8px;margin-bottom:16px}
.gallery{left:573px;top:740px}
.frame{margin-top:4px;width:231px;height:117px;border:1px solid var(--line);padding:5px;background:#fff;box-shadow:0 1px 3px rgba(0,0,0,.1)}
.photo{width:100%;height:100%;background:linear-gradient(90deg,#cfc2a6,#a9b3a6 45%,#8b8b70 65%,#e15b9c 90%)}
.footer{left:0;top:940px;width:859px;height:260px}
.col{top:990px;font-size:11px;color:#fff;line-height:16.8px;white-space:nowrap}
.col h3{font-size:14px;margin-bottom:5px}
.vdiv{top:990px;width:1px;height:96px;background:rgba(255,255,255,.35)}
.nl{font-size:9px;color:#aaa;background:#fff;border-radius:2px;height:19px;width:145px;padding:0 9px;line-height:19px}
.pay{top:1094px;height:18px;background:#fff;border:1px solid #ddd;font-size:8px;font-weight:700;color:var(--orange-dark);text-align:center;line-height:16px}
.bottom{left:0;top:1153px;width:859px;height:47px;background:var(--orange-dark)}
.copy{left:68px;top:1168px;font-size:8px;color:#fff}
.soc{top:1160px;width:20px;height:20px;background:#4b8ed3;border-radius:2px;color:#fff;font-size:5px;text-align:center;line-height:20px;overflow:hidden}
</style>
</head>
<body>

<div class="abs hero" role="img" aria-label="Photo of a tropical beach with turquoise sea, sailboat, white parasol and two wooden deck chairs"></div>

<header class="abs topbar">
  <div class="abs logo"><i></i>Orsabelli travel</div>
  <nav class="abs nav">
    <span>Forum</span><span>My Tour</span><span>Language</span>
    <span>My Cart<svg width="30" height="24" viewBox="0 0 28 22"><path d="M1 3h5l4 12h13l3-9H8" fill="none" stroke="#fff" stroke-width="2.4"/><circle cx="12" cy="19" r="2" fill="#fff"/><circle cx="21" cy="19" r="2" fill="#fff"/></svg></span>
  </nav>
</header>
<div class="abs phone">Phone no. <b>8-800-555-0142</b></div>

<div class="abs tab active" style="left:55px;width:100px">Tickets</div>
<div class="abs tab idle" style="left:158px;width:77px">Info</div>
<div class="abs tab idle" style="left:238px;width:76px">Hotel</div>

<form class="abs panel">
  <span class="abs lbl" style="left:24px;top:28px">Whence</span>
  <div class="abs field" style="left:87px;top:22px;width:146px">type your text</div>
  <span class="abs lbl" style="left:246px;top:28px">Where</span>
  <div class="abs field" style="left:287px;top:22px;width:146px">type your text</div>

  <span class="abs lbl" style="left:23px;top:61px">There</span>
  <div class="abs field val" style="left:85px;top:55px;width:90px">14-06-2013</div>
  <span class="abs lbl" style="left:248px;top:61px">Back</span>
  <div class="abs field" style="left:287px;top:55px;width:91px"></div>
  <div class="abs chk" style="left:385px;top:55px"><i></i>Back</div>
  <div class="abs chk" style="left:385px;top:68px"><i></i>One Way</div>

  <span class="abs lbl" style="left:24px;top:95px">Passengers</span>
  <div class="abs field val sel" style="left:87px;top:91px;width:44px">1<span class="sep"></span></div>
  <div class="abs field val sel" style="left:145px;top:91px;width:44px">0<span class="sep"></span></div>
  <div class="abs field val sel" style="left:202px;top:91px;width:44px">0<span class="sep"></span></div>
  <div class="abs btn" style="left:290px;top:91px;width:88px;height:25px;line-height:25px">Search Now</div>

  <span class="abs lbl" style="left:24px;top:132px">Class</span>
  <div class="abs field val sel" style="left:86px;top:126px;width:89px">Economy<span class="sep"></span></div>
</form>

<svg class="abs" style="left:772px;top:448px" width="32" height="22" viewBox="0 0 32 22"><path d="M11 2 3 11l8 9M21 2l8 9-8 9" fill="none" stroke="#333" stroke-width="1.6"/></svg>

<section class="abs card" style="left:54px">
  <h2 style="color:var(--purple)">BN3bl</h2>
  <p>Duis tincidunt lectus quis dui viverra vestibu-lum. Suspendisse vulputate aliquam dui. Nulla elementum dui ut augue.</p>
  <ol><li>1. Phasellus felis dolor</li><li>2. Scelerisque tempus eget</li><li>3. Lobortis id libero</li></ol>
</section>
<section class="abs card" style="left:312px">
  <h2 style="color:var(--red)">ABNA6NETBI</h2>
  <p>Nunc tempus felis vitae urna. Vivamus portti-tor, g, purus nisi eleifend libero, a tempus libero lectus feugiat felis. Morbi diam mauris, viverra in, gravida eu, mattis in, ante. Morbi eget arcu. Morbi porta, libero id ullamcorper nonummy, nibh ligula pulvinar</p>
</section>
<section class="abs card" style="left:570px">
  <h2 style="color:var(--green)">OTEUN</h2>
  <p>Nunc tempus felis vitae urna. Vivamus portti-tor, g, purus nisi eleifend libero, a tempus libero lectus feugiat felis. Morbi diam mauris, viverra in, gravida eu, mattis in, ante. Morbi eget arcu. Morbi porta, libero id ullamcorper nonummy, nibh ligula pulvinar</p>
</section>

<section class="abs about">
  <h2>About Orsabelli Travel</h2>
  <p>Duis tincidunt lectus quis dui viverra vestibulum. Suspendisse vulputate aliquam dui. Nulla elementum dui ut augue. Aliquam vehicula mi at mauris. Maecenas placerat, nisl at consequat rhoncus, sem nunc gravida justo, quis eleifend arcu velit quis lacus. Morbi magna magna, tincidunt a, mattis non, imperdiet vitae, tellus. Sed odio est, auctor ac, sollicitudin in, consequat vitae, orci. Fusce id felis. Vivamus sollicitudin metus eget eros.</p>
  <p>Mauris vel lacus vitae felis vestibulum volutpat. Etiam est nunc, venenatis in, tristique eu, imperdiet ac, nisl. Cum sociis natoque penatibus et magnis dis parturient montes, nascetur ridiculus mus. In iaculis facilisis massa. Etiam eu urna. Sed porta. Suspendisse quam leo, molestie sed, luctus quis, feugiat in, pede.</p>
</section>

<section class="abs gallery">
  <h2>Our Gallery</h2>
  <div class="frame"><div class="photo" role="img" aria-label="Photo of two young travellers with a guidebook on an old city street"></div></div>
</section>
<svg class="abs" style="left:778px;top:890px" width="24" height="18" viewBox="0 0 24 18"><path d="M8 2 2 9l6 7M16 2l6 7-6 7" fill="none" stroke="#333" stroke-width="1.5"/></svg>

<svg class="abs footer" width="859" height="260" viewBox="0 0 859 260">
  <defs><linearGradient id="fg" x1="0" y1="0" x2="0" y2="1"><stop offset="0" stop-color="#f9922c"/><stop offset="1" stop-color="#f06d1c"/></linearGradient></defs>
  <path d="M0 30Q430 -10 859 22V260H0Z" fill="#e6e6e6"/>
  <path d="M0 33Q430 -6 859 25V260H0Z" fill="url(#fg)"/>
</svg>

<div class="abs col" style="left:66px"><h3>View Site</h3>Home<br>About Us<br>Forum<br>Contacts</div>
<div class="abs vdiv" style="left:157px"></div>
<div class="abs col" style="left:183px"><h3>Help</h3>Help<br>Term of Use<br>Privacy Policy<br>Cookies</div>
<div class="abs vdiv" style="left:267px"></div>
<div class="abs col" style="left:293px"><h3>Contact Info</h3>Trip Welder Limited<br>14 Harbour Lane London, E2 5QT UK<br>Phone: +7 (495) 555-01-86<br>Email: info@tripwelder.com<br>Exclusive Offers</div>
<div class="abs vdiv" style="left:480px"></div>
<div class="abs col" style="left:516px;top:987px"><h3>Newsletter Sign Up</h3></div>
<div class="abs nl" style="left:516px;top:1010px">your name</div>
<div class="abs nl" style="left:516px;top:1035px">email address</div>
<div class="abs btn" style="left:594px;top:1061px;width:67px;height:21px;line-height:21px;background:#f6a25e">Subscribe</div>

<div class="abs pay" style="left:520px;width:30px">Cardo</div>
<div class="abs pay" style="left:553px;width:30px">Rivo</div>
<div class="abs pay" style="left:586px;width:28px">Nexa</div>
<div class="abs pay" style="left:617px;width:53px">PayWell</div>

<div class="abs bottom"></div>
<div class="abs copy">Copyright © 2013 Company Name. All Rights Reserved.</div>
<div class="abs soc" style="left:696px">Chirpo</div>
<div class="abs soc" style="left:719px">Linka</div>
<div class="abs soc" style="left:743px">Facely</div>
<div class="abs soc" style="left:767px">Gloop</div>

</body>
</html>
```